https://velormark.com

We need a cool technology design for our Managed IT Services company. We are located in Coral Springs Florida. We provide all IT services and support for small to medium sized businesses. We would like to see designs that use our blue and white colors from our website.

```html
<!DOCTYPE html>
<html lang="en">
<head>
<meta charset="utf-8">
<title>Velormark Business Card</title>
<link rel="stylesheet" href="https://fonts.googleapis.com/css2?family=Lato:wght@400;700;900&display=swap">
<style>
  :root {
    --backdrop: #2b2219;
    --card: #ffffff;
    --navy: #1b2f53;
    --band-grey: #dcdfe4;
    --text-dark: #2a2d33;
  }
  * { margin: 0; padding: 0; box-sizing: border-box; }
  html, body { width: 1200px; height: 1200px; overflow: hidden; }
  body {
    background: var(--backdrop);
    font-family: "Lato", sans-serif;
    position: relative;
  }
  .card {
    position: absolute;
    background: var(--card);
    border-radius: 24px;
    overflow: hidden;
  }
  .card-front { left: 85px; top: 251px; width: 373px; height: 650px; }
  .card-back  { left: 485px; top: 529px; width: 650px; height: 372px; }

  .wordmark {
    position: absolute;
    left: 0; right: 0;
    text-align: center;
    color: var(--navy);
    font-weight: 900;
    letter-spacing: -0.5px;
    line-height: 1;
  }
  .card-front .wordmark { top: 384px; top: 384px; font-size: 46px; top: 134px; }
  .card-back .wordmark { top: 168px; font-size: 58px; top: 164px; }

  .name-band { position: absolute; left: 25px; top: 284px; width: 324px; height: 46px; }
  .name-band svg { position: absolute; inset: 0; }
  .person-name {
    position: absolute; left: 0; right: 0; top: 0; height: 46px;
    display: flex; align-items: center; justify-content: center;
    color: var(--navy); font-weight: 700; font-size: 25px; letter-spacing: 1px;
  }
  .person-role {
    position: absolute; left: 0; right: 0; top: 335px;
    text-align: center; font-size: 14px; letter-spacing: 1px; color: var(--text-dark);
  }
  .contact-icons {
    position: absolute; left: 0; right: 0; top: 390px;
    display: flex; justify-content: center; gap: 17px;
  }
  .icon-dot {
    width: 27px; height: 27px; border-radius: 50%;
    background: var(--navy); box-shadow: 0 0 0 2px #c9ced6;
    display: flex; align-items: center; justify-content: center;
  }
  .contact-list {
    position: absolute; left: 0; right: 0; top: 429px;
    text-align: center; font-size: 14.5px; letter-spacing: 1.3px; color: var(--text-dark);
    line-height: 24.5px;
  }
  .address-icon { position: absolute; left: 173px; top: 528px; }
  .address {
    position: absolute; left: 0; right: 0; top: 563px;
    text-align: center; font-size: 14.5px; letter-spacing: 1.3px; color: var(--text-dark);
    line-height: 18px;
  }
  .edge-tab { position: absolute; top: 172px; width: 22px; height: 53px; background: var(--navy); }
  .edge-tab.left { left: 0; }
  .edge-tab.right { right: 0; }
</style>
</head>
<body>
  <section class="card card-front">
    <div class="wordmark">VELORMARK</div>

    <div class="name-band">
      <svg width="324" height="46" viewBox="0 0 324 46">
        <polygon points="10,0 324,0 314,46 0,46" fill="var(--band-grey)"/>
        <polygon points="6,6 15,6 8,40 0,40" fill="var(--navy)"/>
        <polygon points="316,6 324,6 317,40 308,40" fill="var(--navy)"/>
      </svg>
      <div class="person-name">DANIEL HARTLEY</div>
    </div>
    <div class="person-role">Founder &amp; CEO</div>

    <div class="contact-icons">
      <div class="icon-dot">
        <svg width="13" height="13" viewBox="0 0 24 24"><path fill="#fff" d="M6.6 10.8a15.5 15.5 0 0 0 6.6 6.6l2.2-2.2c.3-.3.7-.4 1-.2 1.1.4 2.3.6 3.6.6.6 0 1 .4 1 1V20c0 .6-.4 1-1 1A17 17 0 0 1 3 4c0-.6.4-1 1-1h3.5c.6 0 1 .4 1 1 0 1.3.2 2.5.6 3.6.1.3 0 .7-.2 1z"/></svg>
      </div>
      <div class="icon-dot">
        <svg width="13" height="13" viewBox="0 0 24 24"><rect x="3" y="5" width="18" height="14" rx="2" fill="#fff"/><path d="M3 6l9 7 9-7" fill="none" stroke="var(--navy)" stroke-width="2"/></svg>
      </div>
      <div class="icon-dot">
        <svg width="12" height="12" viewBox="0 0 24 24"><path fill="#fff" d="M4 2l16 8-7 2 5 8-3 2-5-8-5 5z"/></svg>
      </div>
    </div>

    <div class="contact-list">
      <div>(954) 555-0142</div>
      <div>hartley@velormark.com</div>
      <div>www.velormark.com</div>
    </div>

    <div class="address-icon">
      <div class="icon-dot">
        <svg width="12" height="14" viewBox="0 0 24 28"><path fill="#fff" d="M12 1a9 9 0 0 0-9 9c0 7 9 17 9 17s9-10 9-17a9 9 0 0 0-9-9zm0 12.5a3.5 3.5 0 1 1 0-7 3.5 3.5 0 0 1 0 7z"/></svg>
      </div>
    </div>
    <div class="address">
      <div>2180 Palm Crest Blvd #410</div>
      <div>Coral Springs, Florida 33065</div>
    </div>
  </section>

  <section class="card card-back">
    <div class="edge-tab left"></div>
    <div class="wordmark">VELORMARK</div>
    <div class="edge-tab right"></div>
  </section>
</body>
</html>
```